Dunmore Hale Voss LLC letterhead/envelope/stationary

Design letterhead and envelope based on prior logo design. Design should be conservative and classic for a defense litigation law firm.

Target Market(s)

Businesses, insurance carriers, construction companies, product manufacturers, healthcare providers, employers, municipalities. In short, the target is businesses that may be sued in court and need civil defense attorneys.

Font styles to use
Serif
Sans Serif

Colors
0255a3

Requirements
Must have
• Straightforward design for letterhead and envelopes including digital format for word. Template should be able to be updated for individual attorneys within the firm. Font should be Trajan Pro if possible to match logo (or a similar font). Firm information is Dunmore Hale Voss LLC, 4700 Westfield Terrace, Suite 320, Birmingham, Alabama, 35817. (205)368-2941. other fields that should be included are fax line, direct line, cell phone and email address so that we can update template for each attorney. The color for the logo is 003362
Nice to have
• digital template for microsoft outlook
Should not have
• Busy design/too many graphics

```html
<!DOCTYPE html>
<html lang="en">
<head>
<meta charset="utf-8">
<title>Dunmore Hale Voss LLC – Stationery</title>
<link rel="stylesheet" href="https://fonts.googleapis.com/css2?family=Cinzel:wght@400;600&family=Raleway:wght@400&display=swap">
<style>
  :root {
    --backdrop: #333030;
    --paper: #ffffff;
    --navy: #17355f;
    --ink: #1f1f1f;
  }
  * { box-sizing: border-box; margin: 0; padding: 0; }
  html, body { width: 1200px; height: 789px; overflow: hidden; background: var(--backdrop); }
  .canvas { position: relative; width: 1200px; height: 789px; }

  .sheet { position: absolute; background: var(--paper); }
  .letterhead { left: 32px; top: 61px; width: 528px; height: 684px; }
  .envelope-front { left: 587px; top: 190px; width: 590px; height: 256px; }
  .envelope-back { left: 587px; top: 488px; width: 590px; height: 257px; }

  .firm-mark { position: absolute; left: 0; right: 0; text-align: center; color: var(--navy); }
  .firm-name {
    font-family: "Cinzel", serif; font-weight: 600;
    font-size: 17px; letter-spacing: 0.5px; line-height: 1.1;
  }
  .firm-tagline {
    font-family: "Raleway", sans-serif; font-size: 4.5px;
    letter-spacing: 1.2px; margin-top: 4px;
  }
  .letterhead .firm-mark { top: 130px; }
  .envelope-front .firm-mark { top: 140px; }
  .envelope-front .firm-name { font-size: 15px; }

  .contact-block {
    position: absolute; left: 0; right: 0; text-align: center;
    font-family: "Raleway", sans-serif; font-size: 8.6px; line-height: 10.8px; color: var(--ink);
  }
  .contact-block .label { font-family: "Cinzel", serif; font-weight: 600; color: var(--navy); }
  .contact-block .sep { margin: 0 4px; }
  .letterhead .contact-block { top: 638px; }
  .envelope-front .contact-block { top: 264px; }
  .envelope-front .contact-block { top: 264px; }
  .envelope-front .contact-block { top: 266px; top: 262px; }

  .envelope-flap { position: absolute; left: 0; top: 0; width: 590px; height: 62px; }
  .envelope-flap .firm-name-light {
    position: absolute; left: 0; right: 0; top: 21px; text-align: center;
    font-family: "Cinzel", serif; font-weight: 600; font-size: 16px; color: var(--paper);
    letter-spacing: 0.5px;
  }
</style>
</head>
<body>
<div class="canvas">

  <section class="sheet letterhead">
    <header class="firm-mark">
      <div class="firm-name">Dunmore . Hale . Voss . LLC</div>
      <div class="firm-tagline">ATTORNEYS AT LAW</div>
    </header>
    <footer class="contact-block">
      <div>4700 Westfield Terrace, Suite 320, Birmingham, Alabama, 35817</div>
      <div><span class="label">P</span> : (000)000-0000<span class="sep">|</span><span class="label">D</span>: (205)368-2941<span class="sep">|</span><span class="label">F</span> : (000)000-0000</div>
      <div><span class="label">E</span> : info@dunmorehalevoss.com<span class="sep">|</span><span class="label">W</span>: www.dunmorehalevoss.com</div>
    </footer>
  </section>

  <section class="sheet envelope-front">
    <header class="firm-mark">
      <div class="firm-name">Dunmore . Hale . Voss . LLC</div>
      <div class="firm-tagline">ATTORNEYS AT LAW</div>
    </header>
    <footer class="contact-block" style="top:219px">
      <div>4700 Westfield Terrace, Suite 320, Birmingham, Alabama, 35817</div>
      <div><span class="label">P</span> : (000)000-0000<span class="sep">|</span><span class="label">D</span>: (205)368-2941<span class="sep">|</span><span class="label">F</span> : (000)000-0000</div>
      <div><span class="label">E</span> : info@dunmorehalevoss.com<span class="sep">|</span><span class="label">W</span>: www.dunmorehalevoss.com</div>
    </footer>
  </section>

  <section class="sheet envelope-back">
    <div class="envelope-flap">
      <svg width="590" height="62" viewBox="0 0 590 62" aria-hidden="true">
        <polygon points="0,0 590,0 562,62 27,62" fill="var(--navy)"/>
      </svg>
      <div class="firm-name-light">Dunmore Hale Voss LLC</div>
    </div>
  </section>

</div>
</body>
</html>
```